Health & Wellness Contest - The Bright Harvest Renewal

We need a postcard design that is professional and grabs the attention of people who see it. The postcard will be left in fitness centers and posted on social media. The front of the card MUST look amazing - make potential participants want to pick it up and find out more information; the back of the card will have the contest details. The goal is to have people sign up for a 90 day fitness program, and most of the marketing will be with this postcard.

Target Market(s)

People that are thinking about beginning a health regiment; people who are already used to exercising and are willing to try a new supplement

Industry/Entity Type

Health And Wellness

Colors

Designer to choose colors to be used in the design.

Requirements
Must have
• Front Cover -- Must have the phrase "The Bright Harvest Renewal" and must have "$2,500 Grand Prize"; and must have "BrightHarvestRenewal.com"
Nice to have
• Design on Front; Details on Back; appeal to both men and women

```html
<!DOCTYPE html>
<html lang="en">
<head>
<meta charset="utf-8">
<title>The Bright Harvest Renewal – Postcard</title>
<link href="https://fonts.googleapis.com/css2?family=Oswald:wght@500;700&family=Montserrat:wght@500;800;900&family=Lato:wght@400;700;900&display=swap" rel="stylesheet">
<style>
:root{
  --page:#ece9e4;
  --royal:#1f4f93;
  --royal-dark:#163a72;
  --navy:#13284f;
  --ink:#1d1f24;
  --silver:#d9dbde;
  --white:#ffffff;
  --link:#2a62ad;
  --charcoal:#3b3c3f;
}
*{box-sizing:border-box;margin:0;padding:0}
html,body{width:1200px;height:1200px;overflow:hidden;background:var(--page)}
.canvas{position:relative;width:1200px;height:1200px}
.card{position:absolute;overflow:hidden;box-shadow:0 6px 18px rgba(0,0,0,.25)}

/* FRONT */
.front{left:114px;top:80px;width:626px;height:484px;
  background:radial-gradient(ellipse at 30% 20%,#fafafa,#dcdcdc 90%)}
.front .brand{position:absolute;left:56px;top:40px;width:240px;text-align:center}
.brand-mark{display:block;width:40px;height:40px;margin:0 auto 8px;background:var(--navy)}
.brand-name{font-family:"Montserrat",sans-serif;font-weight:500;font-size:21px;letter-spacing:1px;color:var(--navy);white-space:nowrap}
.brand-sub{font-family:"Montserrat",sans-serif;font-weight:500;font-size:11px;letter-spacing:3px;color:var(--navy);white-space:nowrap}
.front .band{position:absolute;left:0;top:132px;width:626px;height:240px;
  background:linear-gradient(135deg,var(--royal) 0%,var(--royal-dark) 100%)}
.front .photo-pair{position:absolute;left:330px;top:14px;width:296px;height:350px;
  background:linear-gradient(180deg,#2c3546 0%,#1a2234 60%,#0f1628 100%)}
.title{position:absolute;left:30px;top:150px;font-family:"Oswald",sans-serif;color:var(--silver);line-height:1;white-space:nowrap}
.title .t1{display:block;font-size:40px;font-weight:700;letter-spacing:1px}
.title .t2{display:block;font-family:"Montserrat",sans-serif;font-weight:900;font-size:50px;margin-top:8px;color:#e8e9ec}
.title .t3{display:block;font-size:58px;font-weight:700;margin-top:8px}
.stripe{position:absolute;left:0;width:626px;background:var(--navy)}
.prize-bar{position:absolute;left:120px;top:350px;width:425px;height:68px;background:var(--navy);
  border:3px solid var(--white);border-radius:0 34px 34px 0;
  font-family:"Oswald",sans-serif;font-weight:700;font-size:40px;color:var(--white);
  line-height:62px;padding-left:56px;white-space:nowrap;overflow:hidden}
.medal{position:absolute;left:42px;top:330px;width:112px;height:112px;border-radius:50%;
  background:radial-gradient(circle at 35% 30%,#ffffff,#c7c9cc 70%,#9ea1a6);
  box-shadow:0 3px 8px rgba(0,0,0,.35)}
.medal svg{position:absolute;left:28px;top:24px}
.url{position:absolute;left:150px;top:432px;font-family:"Lato",sans-serif;font-weight:900;
  font-size:21px;letter-spacing:4px;color:var(--ink);white-space:nowrap}

/* BACK */
.back{left:474px;top:650px;width:624px;height:482px;
  background:radial-gradient(ellipse at 70% 40%,#f4f4f4,#cfcfcf 95%)}
.back .faded-photo{position:absolute;left:300px;top:60px;width:324px;height:402px;
  background:radial-gradient(ellipse at 45% 55%,rgba(255,255,255,.7),rgba(200,200,200,0) 70%)}
.intro{position:absolute;left:20px;top:20px;width:272px;font-family:"Lato",sans-serif;
  font-size:12.4px;line-height:15.5px;color:var(--ink)}
.intro p+p{margin-top:15px;text-align:justify}
.benefits{position:absolute;left:0;top:114px;width:300px;height:130px;
  background:linear-gradient(135deg,var(--royal-dark),var(--navy));padding:8px 0 0 24px;
  display:flex;gap:16px;font-family:"Lato",sans-serif;font-size:16px;line-height:18.6px;color:var(--white)}
.benefits ul{list-style:none;width:125px}
.benefits li{position:relative;padding-left:18px}
.benefits li::before{content:"";position:absolute;left:2px;top:6px;width:8px;height:4px;
  border-left:1.5px solid var(--white);border-bottom:1.5px solid var(--white);transform:rotate(-45deg)}
.athlete{position:absolute;left:0;top:258px;width:148px;height:224px;
  background:linear-gradient(160deg,#b79a86 0%,#6f6f72 45%,#2b2c30 100%)}
.gp-label{position:absolute;left:150px;top:262px;width:150px;text-align:right;
  font-family:"Lato",sans-serif;font-size:24px;color:var(--ink);white-space:nowrap}
.gp-pill{position:absolute;left:98px;top:294px;width:200px;height:36px;background:var(--navy);
  border:2px solid var(--white);border-radius:0 18px 18px 0;text-align:center;
  font-family:"Lato",sans-serif;font-weight:900;font-style:italic;font-size:24px;line-height:32px;color:var(--white)}
.deadlines-h{position:absolute;left:158px;top:338px;width:142px;text-align:center;
  font-family:"Lato",sans-serif;font-size:14px;color:var(--link);white-space:nowrap}
.deadlines{position:absolute;left:150px;top:360px;width:154px;height:52px;background:var(--ink);
  border-radius:6px;padding:5px 9px;font-family:"Lato",sans-serif;font-size:8.6px;line-height:11px;color:var(--white)}
.contact{position:absolute;left:182px;top:420px;font-family:"Lato",sans-serif;font-weight:700;
  font-size:9.6px;line-height:12px;color:var(--ink);white-space:nowrap}
.contact .email{color:var(--royal-dark)}
.contact .web{display:flex;align-items:center;gap:5px;margin-top:5px;margin-left:-14px}
.contact .web i{width:7px;height:7px;border-radius:50%;background:var(--royal-dark)}
.back .brand{position:absolute;left:345px;top:64px;width:120px;text-align:center}
.back .brand-mark{width:20px;height:20px;margin-bottom:4px}
.back .brand-name{font-size:10px;letter-spacing:.4px}
.back .brand-sub{font-size:5.5px;letter-spacing:1.2px}
.stamp{position:absolute;left:507px;top:36px;width:78px;height:77px;background:#5d5e61}
.address-line{position:absolute;left:357px;width:248px;height:1px;background:#6d6e71}
.foot{position:absolute;left:0;top:462px;width:624px;height:20px;background:var(--charcoal)}
</style>
</head>
<body>
<div class="canvas">

  <section class="card front" aria-label="Postcard front">
    <div class="brand">
      <span class="brand-mark"></span>
      <div class="brand-name">KEYSTONE RIDGE</div>
      <div class="brand-sub">Group - LLC</div>
    </div>
    <div class="band"></div>
    <div class="photo-pair" role="img" aria-label="Photo of a man and a woman in gym wear holding dumbbells"></div>
    <h1 class="title">
      <span class="t1">THE BRIGHT</span>
      <span class="t2">HARVEST</span>
      <span class="t3">RENEWAL</span>
    </h1>
    <div class="stripe" style="top:368px;height:12px"></div>
    <div class="stripe" style="top:388px;height:16px"></div>
    <div class="prize-bar">$2,500 GRAND PRIZE</div>
    <div class="medal">
      <svg width="56" height="64" viewBox="0 0 56 64" aria-hidden="true">
        <path d="M14 4h28v14c0 12-6 20-14 20S14 30 14 18z" fill="#1a1c20"/>
        <path d="M14 10H4c0 12 6 18 12 18M42 10h10c0 12-6 18-12 18" fill="none" stroke="#1a1c20" stroke-width="4"/>
        <rect x="25" y="37" width="6" height="12" fill="#1a1c20"/>
        <rect x="16" y="50" width="24" height="5" fill="#1a1c20"/>
        <rect x="13" y="58" width="30" height="4" fill="#1a1c20"/>
      </svg>
    </div>
    <div class="url">BrightHarvestRenewal.com</div>
  </section>

  <section class="card back" aria-label="Postcard back">
    <div class="faded-photo" role="img" aria-label="Faded photo of a dumbbell"></div>
    <div class="intro">
      <p>The Bright Harvest Renewal has one mission – to help people be a <b>better</b> version of themselves.</p>
      <p>Join us in the Bright Harvest Renewal fitness program and experience some of the benefits that countless others have seen:</p>
    </div>
    <div class="benefits">
      <ul><li>Better health</li><li>Appetite suppression</li><li>Better energy</li><li>Better mood</li><li>Better sleep</li></ul>
      <ul><li>Fat Loss</li><li>Better focus</li><li>Increased awareness</li><li>Muscle preservation</li></ul>
    </div>
    <div class="athlete" role="img" aria-label="Photo of a man training with weights"></div>
    <div class="gp-label">Grand Prize:</div>
    <div class="gp-pill">$2,500.00</div>
    <div class="deadlines-h">Challenge Deadlines</div>
    <div class="deadlines">Registration Periods end Sept. 31st, Dec. 31st, March 31st, and June 30th.</div>
    <div class="contact">
      <div>For more information, email</div>
      <div class="email">info@KeystoneRidge.org</div>
      <div class="web"><i></i>www.BrightHarvestRenewal.com</div>
    </div>
    <div class="brand">
      <span class="brand-mark"></span>
      <div class="brand-name">KEYSTONE RIDGE</div>
      <div class="brand-sub">Group - LLC</div>
    </div>
    <div class="stamp" aria-label="Stamp area"></div>
    <div class="address-line" style="top:171px"></div>
    <div class="address-line" style="top:207px"></div>
    <div class="address-line" style="top:246px"></div>
    <div class="address-line" style="top:282px"></div>
    <div class="address-line" style="top:319px"></div>
    <div class="foot"></div>
  </section>

</div>
</body>
</html>
```